Visitenkarten-Design für Unternehmensberatung
Zielgruppe
Unternehmensberatung, Auswanderungsberatung und Firmengründung in Dubai. Wir suchen ein modernes Design. unserer Zielgruppe sind deutschsprachige Unternehmer
Aufgabenstellung
Lukas Brandtner - CEO
Adresse: Harbor Crest Park, Building C7, Dubai, VAE
EMail: kontakt@terravia-plan.de
WhatsApp: +49 1764093217
Mobil: +971 563841072
www.terravia-plan.de
(Instagram: https://www.instagram.com/terravia.plan/)

```html
<!DOCTYPE html>
<html lang="de">
<head>
<meta charset="utf-8">
<title>Terravia Plan – Visitenkarte</title>
<link rel="stylesheet" href="https://fonts.googleapis.com/css2?family=Montserrat:wght@500;700&family=Roboto:wght@300&display=swap">
<style>
  :root {
    --navy: #0f1f2f;
    --cyan: #0596c2;
    --paper: #ffffff;
    --stage: #ffffff;
    --mark: #d6d6d6;
    --ink: #111111;
  }
  * { margin: 0; padding: 0; box-sizing: border-box; }
  html, body {
    width: 1200px; height: 1200px; overflow: hidden;
    background: var(--stage);
  }
  .canvas { position: relative; width: 1200px; height: 1200px; }
  .card {
    position: absolute; width: 748px; height: 427px;
    background: var(--paper); overflow: hidden;
  }
  .card--front { left: 259px; top: 124px; }
  .card--back { left: 260px; top: 656px; }
  .card__shapes { position: absolute; inset: 0; width: 748px; height: 427px; }

  .brand { position: absolute; display: flex; align-items: center; }
  .brand__dot { border-radius: 50%; background: var(--mark); flex: none; }
  .brand__name {
    font-family: "Montserrat", sans-serif; font-weight: 700;
    color: var(--ink); white-space: nowrap; letter-spacing: 0.01em;
  }
  .card--front .brand { left: 46px; top: 170px; gap: 9px; }
  .card--front .brand__dot { width: 48px; height: 48px; }
  .card--front .brand__name { font-size: 19px; }
  .card--back .brand { left: 134px; top: 170px; gap: 20px; }
  .card--back .brand__dot { width: 102px; height: 102px; }
  .card--back .brand__name { font-size: 40px; }

  .person {
    position: absolute; left: 307px; width: 441px; top: 58px;
    text-align: center; color: var(--paper);
  }
  .person__name {
    font-family: "Montserrat", sans-serif; font-weight: 700;
    font-size: 36px; line-height: 1.2; white-space: nowrap;
  }
  .person__role {
    font-family: "Roboto", sans-serif; font-weight: 300;
    font-size: 22px; margin-top: 4px;
  }
  .contact { position: absolute; left: 368px; top: 170px; list-style: none; }
  .contact__item {
    display: flex; align-items: center; height: 26px; margin-bottom: 13px;
    font-family: "Montserrat", sans-serif; font-weight: 500;
    font-size: 17px; letter-spacing: 0.05em; color: var(--paper);
    white-space: nowrap;
  }
  .contact__icon { width: 22px; height: 22px; margin-right: 18px; flex: none; }
</style>
</head>
<body>
<main class="canvas">

  <section class="card card--front" aria-label="Vorderseite">
    <svg class="card__shapes" viewBox="0 0 1197 684" preserveAspectRatio="none" aria-hidden="true">
      <polygon points="0,0 161,0 84,73 0,73" fill="var(--navy)"/>
      <polygon points="198,0 363,0 286,73 119,73" fill="var(--cyan)"/>
      <rect x="492" y="0" width="705" height="588" fill="var(--navy)"/>
      <polygon points="0,610 161,610 84,684 0,684" fill="var(--navy)"/>
      <polygon points="198,610 363,610 286,684 119,684" fill="var(--cyan)"/>
      <polygon points="411,610 1197,610 1197,684 336,684" fill="var(--navy)"/>
      <polygon points="532,610 698,610 622,684 454,684" fill="var(--cyan)"/>
    </svg>

    <div class="brand">
      <span class="brand__dot"></span>
      <span class="brand__name">TERRAVIA PLAN</span>
    </div>

    <div class="person">
      <h1 class="person__name">Lukas Brandtner</h1>
      <p class="person__role">CEO</p>
    </div>

    <ul class="contact">
      <li class="contact__item">
        <svg class="contact__icon" viewBox="0 0 24 24" aria-hidden="true">
          <circle cx="12" cy="12" r="10.5" fill="none" stroke="#fff" stroke-width="2"/>
          <path d="M8.3 7.2c.6-.5 1.3-.4 1.6.2l.9 1.7c.3.6.1 1.1-.4 1.5l-.5.4c.6 1.4 1.6 2.5 3 3.2l.5-.5c.4-.5 1-.6 1.5-.3l1.6 1c.6.4.6 1.1.1 1.6-1 1-2.3 1.3-3.6.6-2.2-1.2-3.9-3-4.9-5.2-.5-1.3-.3-3.1.2-4.2z" fill="#fff"/>
        </svg>
        +971 563841072
      </li>
      <li class="contact__item">
        <svg class="contact__icon" viewBox="0 0 24 24" aria-hidden="true">
          <circle cx="12" cy="12" r="10.5" fill="none" stroke="#fff" stroke-width="2"/>
          <path d="M5 9c2-1 3-3 5-2 1 1 0 3 2 3s2 2 1 3-3 0-4 2-1 3-3 2c-1-2 0-3-1-5S4 10 5 9zM15 5c2 1 3 2 4 4-1 1-3 0-3 2s2 2 3 3c-1 2-2 3-4 4 0-2 1-3 0-4s-2-2-1-4 2-2 1-5z" fill="#fff"/>
        </svg>
        www.terravia-plan.de
      </li>
      <li class="contact__item">
        <svg class="contact__icon" viewBox="0 0 24 24" aria-hidden="true">
          <rect x="1.5" y="5" width="21" height="14" fill="none" stroke="#fff" stroke-width="1.6"/>
          <path d="M1.5 5l10.5 8 10.5-8M1.5 19l8-7M22.5 19l-8-7" fill="none" stroke="#fff" stroke-width="1.6"/>
        </svg>
        kontakt@terravia-plan.de
      </li>
      <li class="contact__item">
        <svg class="contact__icon" viewBox="0 0 24 24" aria-hidden="true">
          <path d="M12 1.5a8 8 0 0 0-8 8c0 5.5 8 13 8 13s8-7.5 8-13a8 8 0 0 0-8-8zm0 11.5a3.5 3.5 0 1 1 0-7 3.5 3.5 0 0 1 0 7z" fill="#fff" fill-rule="evenodd"/>
        </svg>
        Harbor Crest Park, Building C7
      </li>
    </ul>
  </section>

  <section class="card card--back" aria-label="Rückseite">
    <svg class="card__shapes" viewBox="0 0 1197 684" preserveAspectRatio="none" aria-hidden="true">
      <polygon points="0,589 854,589 781,684 0,684" fill="var(--navy)"/>
      <polygon points="569,589 737,589 658,684 491,684" fill="var(--cyan)"/>
    </svg>

    <div class="brand">
      <span class="brand__dot"></span>
      <span class="brand__name">TERRAVIA PLAN</span>
    </div>
  </section>

</main>
</body>
</html>
```